KVOR Membership Web Design Project

We need a website design for KVOR membership. We need something different from what we currently have. See what we currently have: http://www.travsel.example/mlm2/

Make provision for where members bushiness can be advertised.
Updates

We need a box for advertising members projects/business.

Make provision for where members bushiness / products can be advertised.

Target Market(s)

For members of KVOR and Intending members. Membership is for married men only.

Requirements
Must have
• Make provision for where members bushiness can be advertised.

You are to redesign: http://www.travsel.example/mlm2/

```html
<!DOCTYPE html>
<html lang="en">
<head>
<meta charset="utf-8">
<title>KVOR Members Portal</title>
<link rel="stylesheet" href="https://fonts.googleapis.com/css2?family=Arimo:wght@400;700&display=swap">
<style>
:root{
  --navy:#0b4a80;
  --blue:#0f5f98;
  --blue-deep:#063c6b;
  --panel:#f2f1ec;
  --panel-grey:#e6e5e0;
  --ink:#333333;
  --ink-soft:#5e5e5e;
  --green:#8cc63f;
  --link-green:#7ab72e;
  --white:#ffffff;
  --field-line:#b9b9b9;
}
*{box-sizing:border-box;margin:0;padding:0}
html,body{width:1085px;height:1200px;overflow:hidden;background:var(--white)}
body{font-family:"Arimo",Arial,sans-serif;color:var(--ink);position:relative}
.top-band{position:absolute;left:0;top:0;width:1085px;height:510px;
  background:linear-gradient(180deg,var(--blue) 0%,#0a5089 60%,var(--blue-deep) 100%)}
.header{position:absolute;left:21px;top:0;width:1041px;height:119px;background:var(--panel);
  border-radius:0 0 6px 6px}
.brand{position:absolute;left:18px;top:28px;display:flex;align-items:center;gap:12px}
.brand-mark{width:62px;height:62px;border-radius:50%;background:var(--navy)}
.brand-name{font-size:22px;font-weight:700;color:var(--navy);line-height:1.2;width:190px}
.login{position:absolute;left:698px;top:36px;width:320px}
.field{position:absolute;top:0;width:155px;height:23px;background:var(--white);border:1px solid var(--field-line);
  font-size:11px;color:var(--ink-soft);padding:4px 8px}
.field.user{left:0}.field.pass{left:165px}
.login-btn{position:absolute;left:0;top:34px;width:82px;height:21px;border-radius:2px;
  background:linear-gradient(180deg,#a3d65a,var(--green));color:var(--white);font-size:13px;text-align:center;line-height:21px}
.forgot{position:absolute;left:96px;top:38px;font-size:11px;color:var(--blue)}
.nav{position:absolute;left:21px;top:131px;width:1041px;height:24px;display:flex;align-items:center}
.nav-item{font-size:13px;color:var(--white);padding:0 18px;border-left:1px dotted rgba(255,255,255,.45);line-height:16px}
.nav-item:first-child{border-left:none;padding-left:27px}
.nav-item.active{color:var(--green)}
.search{position:absolute;left:865px;top:131px;width:183px;height:24px;background:#2574ad;border-radius:2px;
  font-size:10px;color:var(--white);padding:6px 9px}
.search svg{position:absolute;right:7px;top:5px}
.hero{position:absolute;left:21px;top:167px;width:1041px;height:322px;background:var(--panel);border-radius:5px;overflow:hidden}
.hero-photo{position:absolute;right:0;top:0;width:510px;height:322px;
  background:linear-gradient(180deg,#f4f5f7 0%,#e9ecef 55%,#7d9a46 72%,#3a2b1f 100%)}
.hero-words{position:absolute;left:68px;top:58px;list-style:none}
.hero-words li{font-size:38px;letter-spacing:1px;color:var(--ink-soft);line-height:56px}
.hero-arrow{position:absolute;top:153px}
.hero-arrow.prev{left:14px}.hero-arrow.next{right:14px}
.feature{position:absolute;top:528px;width:333px;height:157px;border-radius:5px 5px 3px 3px;overflow:hidden;
  box-shadow:0 1px 3px rgba(0,0,0,.35)}
.feature-title{height:49px;background:var(--navy);color:var(--white);font-size:17px;white-space:nowrap;
  padding:17px 44px 0 17px;position:relative}
.feature-title svg{position:absolute;right:11px;top:14px}
.feature-photo{height:108px}
.f1{left:21px}.f1 .feature-photo{background:linear-gradient(135deg,#1d4f8c,#5d93cf 60%,#cfe0f1)}
.f2{left:375px}.f2 .feature-photo{background:linear-gradient(90deg,#1c1612 0 16%,#f3f0ea 16%,#d9d4cb)}
.f3{left:728px}.f3 .feature-photo{background:linear-gradient(160deg,#eaeaea,#c9c9c9 60%,#9a8a5e)}
.welcome{position:absolute;left:21px;top:722px;width:1041px}
.welcome h1{font-size:23px;font-weight:400;color:var(--navy);margin-bottom:7px}
.welcome p{font-size:14.5px;line-height:19.5px;color:var(--ink);margin-bottom:11px}
.read-more{color:var(--link-green);font-size:13px}
.welcome .read-more{display:block;text-align:right;margin-top:-4px}
.promo{position:absolute;top:921px;height:162px;overflow:hidden}
.promo.saving{left:21px;width:510px;background:var(--panel-grey)}
.promo.business{left:552px;width:510px;background:var(--panel)}
.promo-photo{position:absolute;left:0;top:0;height:162px}
.saving .promo-photo{width:200px;background:linear-gradient(135deg,#d79a63,#8c4a22 50%,#3a2a20)}
.business .promo-photo{width:263px;background:linear-gradient(135deg,#cfe3f5,#5f97cf 55%,#e6f0f9)}
.promo-text{position:absolute;font-size:14px;line-height:19.5px;color:var(--ink)}
.saving .promo-text{left:227px;top:28px;width:262px}
.saving .read-more{position:absolute;left:408px;top:132px}
.business h2{position:absolute;left:280px;top:27px;font-size:19px;font-weight:400;color:var(--navy);letter-spacing:.5px}
.business .promo-text{left:280px;top:59px;width:200px}
.business svg{position:absolute;left:467px;top:124px}
.footer{position:absolute;left:0;top:1113px;width:1085px;height:87px;background:var(--navy);
  color:var(--white);font-size:14px;text-align:center;padding-top:34px}
</style>
</head>
<body>
<div class="top-band"></div>

<header class="header">
  <div class="brand">
    <span class="brand-mark"></span>
    <span class="brand-name">Kingdom Voices members portal</span>
  </div>
  <div class="login">
    <div class="field user">Username</div>
    <div class="field pass">Password</div>
    <div class="login-btn">Login</div>
    <div class="forgot">Forgot Password ?</div>
  </div>
</header>

<nav class="nav">
  <span class="nav-item active">HOME</span>
  <span class="nav-item">ABOUT US</span>
  <span class="nav-item">MEMBERSHIP</span>
  <span class="nav-item">MEMBER PROJECTS</span>
  <span class="nav-item">MEMBERSHIP LEVELS</span>
  <span class="nav-item">LINKS</span>
  <span class="nav-item">CONTACT US</span>
</nav>
<div class="search">Search
  <svg width="13" height="13" viewBox="0 0 13 13"><circle cx="5.5" cy="5.5" r="4" fill="none" stroke="#fff" stroke-width="1.4"/><line x1="8.5" y1="8.5" x2="12" y2="12" stroke="#fff" stroke-width="1.6"/></svg>
</div>

<section class="hero">
  <div class="hero-photo" role="img" aria-label="Seedlings sprouting from dark soil in growth stages"></div>
  <ul class="hero-words">
    <li>LOANS</li><li>INVESTMENTS</li><li>INTERESTS</li><li>COMMISSIONS</li>
  </ul>
  <svg class="hero-arrow prev" width="30" height="30" viewBox="0 0 30 30"><circle cx="15" cy="15" r="14" fill="#7f9fbd"/><path d="M17.5 9 11.5 15l6 6" fill="none" stroke="#fff" stroke-width="3"/></svg>
  <svg class="hero-arrow next" width="30" height="30" viewBox="0 0 30 30"><circle cx="15" cy="15" r="14" fill="#7f9fbd"/><path d="M12.5 9l6 6-6 6" fill="none" stroke="#fff" stroke-width="3"/></svg>
</section>

<article class="feature f1">
  <div class="feature-title">OUR OBJECTIVES
    <svg width="22" height="22" viewBox="0 0 22 22"><circle cx="11" cy="11" r="10" fill="#c9d6e3"/><path d="M5 11h10M11 6.5 15.5 11 11 15.5" fill="none" stroke="#0b4a80" stroke-width="2.6"/></svg></div>
  <div class="feature-photo" role="img" aria-label="Man climbing a ladder over a globe against a blue sky"></div>
</article>
<article class="feature f2">
  <div class="feature-title">MEMBERSHIP LEVELS/BENEFITS
    <svg width="22" height="22" viewBox="0 0 22 22"><circle cx="11" cy="11" r="10" fill="#c9d6e3"/><path d="M5 11h10M11 6.5 15.5 11 11 15.5" fill="none" stroke="#0b4a80" stroke-width="2.6"/></svg></div>
  <div class="feature-photo" role="img" aria-label="Typewritten word membership on paper"></div>
</article>
<article class="feature f3">
  <div class="feature-title">REGISTRATION
    <svg width="22" height="22" viewBox="0 0 22 22"><circle cx="11" cy="11" r="10" fill="#c9d6e3"/><path d="M5 11h10M11 6.5 15.5 11 11 15.5" fill="none" stroke="#0b4a80" stroke-width="2.6"/></svg></div>
  <div class="feature-photo" role="img" aria-label="Fountain pen resting on a ring-bound notebook"></div>
</article>

<section class="welcome">
  <h1>WELCOME TO KINGDOM VOICES</h1>
  <p>Kingdom Voices of Righteousness Fellowship (KVOR) was established on the 19th day of July 2008 by a group of Christian men from various Church denominations. KVOR is an interdenominational and non-denominational fellowship, born out of a great and overwhelming burden for our generation and a strong desire to see the kingdom of God come and His will be done on Earth as it is in Heaven</p>
  <p>Kingdom Voices of Righteousness Fellowship (KVOR) was established on the 19th day of July 2008 by a group of Christian men from various Church denominations. KVOR is an interdenominational and non-denominational fellowship, born out of a great and overwhelming burden for our generation and a strong desire to see the kingdom of God come and His will be done on Earth as it is in Heaven</p>
  <span class="read-more">Read More</span>
</section>

<article class="promo saving">
  <div class="promo-photo" role="img" aria-label="Hand stacking copper coins beside the phrase learn the saving culture"></div>
  <p class="promo-text">Kingdom Voices of Righteousness Fellowship (KVOR) was established on the 19th day of July 2008 by a group of Christian men from various Church denominations.</p>
  <span class="read-more">Read More</span>
</article>

<article class="promo business">
  <div class="promo-photo" role="img" aria-label="Small globe on a stand beside a phone in soft blue light"></div>
  <h2>MEMBERS BUSINESS</h2>
  <p class="promo-text">Lorem Ipsum is simply dummy text of the printing and typesetting industry.</p>
  <svg width="24" height="24" viewBox="0 0 24 24"><circle cx="12" cy="12" r="11.5" fill="#0b3f6e"/><path d="M6 12h10M12 7l5 5-5 5" fill="none" stroke="#fff" stroke-width="2.6"/></svg>
</article>

<footer class="footer">©2012 &nbsp;- Terms of Service - Privacy Policy - Program Policies</footer>
</body>
</html>
```